PowerPoint Slide

Next Steps slide to be more professional and visually appealing. Slides 1 to show the existing colors/font. Slide 2 - my idea of color blocking left side of slide with blue. Keep it in an easy format that we can modify if we need to change text or add any other steps.

```html
<!DOCTYPE html>
<html lang="en">
<head>
<meta charset="utf-8">
<title>Next Steps</title>
<link rel="stylesheet" href="https://fonts.googleapis.com/css2?family=PT+Sans:wght@400;700&family=Caladea&display=swap">
<style>
  :root{
    --navy:#1f3461;
    --navy-dark:#213459;
    --accent-red:#c8103a;
    --panel-blue:#e4eefa;
    --page:#ffffff;
    --body-grey:#4a4a4a;
    --rule:#c3c8d0;
    --footer-grey:#b5b9c0;
  }
  *{box-sizing:border-box;margin:0;padding:0}
  html,body{width:1200px;height:675px;overflow:hidden;background:var(--page)}
  .slide{position:relative;width:1200px;height:675px;background:var(--page);font-family:"PT Sans",Arial,sans-serif;color:var(--navy)}
  .color-block{position:absolute;left:0;top:0;width:802px;height:675px;background:var(--panel-blue)}
  .slide-title{position:absolute;left:69px;top:74px;font-size:45px;font-weight:700;color:var(--navy);letter-spacing:.2px}
  .rule{position:absolute;left:60px;width:1076px;height:1px;background:var(--rule)}
  .step-number{position:absolute;width:37px;height:37px;border-radius:50%;background:var(--accent-red);color:#fff;font-weight:700;font-size:25px;display:flex;align-items:center;justify-content:center}
  .step-icon{position:absolute;width:40px;height:40px}
  .step-title{position:absolute;left:167px;font-size:21px;font-weight:700;color:var(--navy);line-height:29px}
  .step-desc{position:absolute;font-size:15px;color:var(--body-grey);line-height:19.5px}
  .timing{position:absolute;left:610px;width:169px;height:30px;background:var(--navy-dark);border-radius:3px;color:#fff;font-family:"Caladea",Georgia,serif;font-size:14px;display:flex;align-items:center;padding-left:10px}
  .rationale{position:absolute;left:820px;font-size:15px;color:var(--body-grey);line-height:19.7px}
  .page-number{position:absolute;left:9px;top:636px;font-size:10px;color:var(--footer-grey)}
  .confidential{position:absolute;left:1031px;top:636px;font-size:10px;color:var(--footer-grey)}
</style>
</head>
<body>
<div class="slide">
  <div class="color-block"></div>
  <h1 class="slide-title">Next Steps</h1>

  <!-- Step 1 -->
  <div class="step-number" style="left:60px;top:182px">1</div>
  <svg class="step-icon" style="left:104px;top:181px" viewBox="0 0 40 40" aria-hidden="true">
    <circle cx="20" cy="20" r="18" fill="var(--navy)"/>
    <text x="20" y="27.5" text-anchor="middle" font-family="PT Sans,Arial,sans-serif" font-weight="700" font-size="22" fill="#fff">$</text>
  </svg>
  <div class="step-title" style="top:186px">2026 Lumen Select Savings</div>
  <p class="step-desc" style="left:153px;top:219px">Veridane to confirm how Lumen Select savings will be<br>leveraged and if savings will be returned to brands</p>
  <div class="timing" style="top:199px">Timing: ASAP</div>
  <p class="rationale" style="top:197px">to ensure there is sufficient time to<br>educate brand teams on the new savings<br>opportunity prior to Upfront commitment</p>

  <div class="rule" style="top:280px"></div>

  <!-- Step 2 -->
  <div class="step-number" style="left:60px;top:299px">2</div>
  <svg class="step-icon" style="left:97px;top:302px;width:54px;height:52px" viewBox="0 0 54 52" aria-hidden="true">
    <path d="M27 2 A11 11 0 1 1 16 13 L27 13 Z" fill="var(--navy)"/>
    <path d="M25 0 A11 11 0 0 0 14 11 L25 11 Z" fill="var(--navy)"/>
    <g stroke="var(--navy)" stroke-width="1.8" fill="none" stroke-linecap="round">
      <path d="M20 26 L11 34"/><path d="M11 34 l0-4 M11 34 l4 0"/>
      <path d="M27 26 L27 34"/><path d="M24 31 l3 3 l3-3"/>
      <path d="M34 26 L43 34"/><path d="M43 34 l0-4 M43 34 l-4 0"/>
    </g>
    <g fill="var(--navy)">
      <circle cx="9" cy="43" r="7"/><circle cx="27" cy="43" r="7"/><circle cx="45" cy="43" r="7"/>
    </g>
    <g font-family="PT Sans,Arial,sans-serif" font-weight="700" font-size="10" fill="#fff" text-anchor="middle">
      <text x="9" y="46.5">$</text><text x="27" y="46.5">$</text><text x="45" y="46.5">$</text>
    </g>
  </svg>
  <div class="step-title" style="top:304px">2026 Hard Savings Allocation/ Distribution</div>
  <p class="step-desc" style="left:167px;top:336px">Veridane to confirm % of savings that brand teams will<br>receive in 2026</p>
  <div class="timing" style="top:336px">Timing: By September</div>
  <p class="rationale" style="top:340px">as brand teams will be presenting<br>tactical plans in October</p>

  <div class="rule" style="top:403px"></div>

  <!-- Step 3 -->
  <div class="step-number" style="left:60px;top:420px">3</div>
  <svg class="step-icon" style="left:106px;top:419px" viewBox="0 0 40 40" aria-hidden="true">
    <g fill="var(--navy)">
      <circle cx="20" cy="9" r="6.5"/>
      <g transform="translate(20 9)">
        <rect x="-1.6" y="-9" width="3.2" height="4"/><rect x="-1.6" y="5" width="3.2" height="4"/>
        <rect x="-9" y="-1.6" width="4" height="3.2"/><rect x="5" y="-1.6" width="4" height="3.2"/>
        <g transform="rotate(45)"><rect x="-1.6" y="-9" width="3.2" height="4"/><rect x="-1.6" y="5" width="3.2" height="4"/><rect x="-9" y="-1.6" width="4" height="3.2"/><rect x="5" y="-1.6" width="4" height="3.2"/></g>
      </g>
      <circle cx="9" cy="25" r="3.6"/><circle cx="20" cy="24" r="4"/><circle cx="31" cy="25" r="3.6"/>
      <path d="M2 38 a7 7 0 0 1 14 0 Z"/><path d="M12 38 a8 8 0 0 1 16 0 Z"/><path d="M24 38 a7 7 0 0 1 14 0 Z"/>
    </g>
    <circle cx="20" cy="9" r="2.8" fill="var(--panel-blue)"/>
    <path d="M18.4 9 l1.2 1.2 l2.2-2.4" stroke="var(--navy)" stroke-width="1.2" fill="none"/>
  </svg>
  <div class="step-title" style="top:425px">2026 Staffing &amp; Scope Approach</div>
  <div class="timing" style="top:436px">Timing: Q3, 2025</div>
  <p class="rationale" style="top:437px">KS, DSO and Procurement to<br>begin discussions</p>

  <div class="rule" style="top:499px"></div>

  <!-- Step 4 -->
  <div class="step-number" style="left:60px;top:518px">4</div>
  <svg class="step-icon" style="left:106px;top:524px" viewBox="0 0 40 40" aria-hidden="true">
    <g fill="var(--navy)">
      <rect x="0" y="4" width="4.5" height="24" rx="1"/>
      <path d="M0 28 L4.5 28 L2.25 34 Z"/>
      <circle cx="2.25" cy="2" r="2"/>
      <rect x="8" y="0" width="28" height="40" rx="2"/>
    </g>
    <g stroke="#fff" stroke-width="2.2" stroke-linecap="round">
      <path d="M13 7 H30"/><path d="M13 12 H30"/><path d="M13 17 H30"/><path d="M13 22 H30"/>
    </g>
    <path d="M13 32 c3-5 4 3 7-1 s3 2 6 0" stroke="#fff" stroke-width="1.8" fill="none" stroke-linecap="round"/>
  </svg>
  <div class="step-title" style="top:522px">2026 and Beyond Contract Extension<br>Proposal</div>
  <div class="timing" style="top:533px">Timing: Q3, 2025</div>
  <p class="rationale" style="top:522px">KS and Veridane to begin<br>discussions</p>

  <div class="page-number">1</div>
  <div class="confidential">Confidential &amp; Proprietary</div>
</div>
</body>
</html>
```